Flyer Rework for Accountants and Lawyers

Information flyer for accountants and lawyers. Text and flowchart provided. Just need to make it look presentable for print and email. Needs to add logo (AI file provided) and provide graphics. No more than two pages. Our corporate visual identify guidelines are attached (MUST Use). Completed on both AI file and PPTX file.
Target Market(s)
Accountants, Company Directors and Lawyers
Industry/Entity Type
Finance And Accounting
Requirements
Must have
- Our corporate visual identify guidelines are attached (MUST Use)

```html
<!DOCTYPE html>
<html lang="en">
<head>
<meta charset="utf-8">
<title>Northbay Advisory – Director Penalty Notices</title>
<link href="https://fonts.googleapis.com/css2?family=Arimo:wght@400;700&display=swap" rel="stylesheet">
<style>
:root{
  --stage:#bdbec0;
  --paper:#ffffff;
  --green:#8dc63f;
  --green-dark:#76b52a;
  --sky:#6dcde0;
  --sky-deep:#5cc6dc;
  --navy:#364057;
  --slate:#5d5e60;
  --box-dark:#58595b;
  --ink:#3a3a3c;
  --row-a:#f1f1f2;
  --row-b:#e6e7e8;
}
*{box-sizing:border-box;margin:0;padding:0}
html,body{width:1200px;height:990px;overflow:hidden}
body{background:var(--stage);font-family:"Arimo",Arial,sans-serif;color:var(--ink);position:relative}
.page{position:absolute;top:155px;width:525px;height:679px;background:var(--paper);box-shadow:0 1px 4px rgba(0,0,0,.25);overflow:hidden}
.page--front{left:63px}
.page--back{left:616px}
.abs{position:absolute}
.brand{display:flex;align-items:center;gap:6px}
.brand__dot{width:50px;height:50px;border-radius:50%;border:4px solid var(--green)}
.brand__name{font-size:11px;font-weight:700;color:var(--slate);letter-spacing:.3px}
.brand__tag{font-size:5.5px;color:var(--slate);margin-top:2px}
.contact{font-size:9.5px;line-height:14px;color:var(--ink)}
.contact li{list-style:none;display:flex;align-items:center;gap:6px}
.contact svg{width:8px;height:8px;fill:var(--slate)}
.contact strong{font-weight:700}
.hero{left:0;top:102px;width:525px;height:167px;background:linear-gradient(180deg,#4f86b8 0%,#c9a47a 38%,#f2b25a 48%,#3aa6c8 60%,#2bb3cf 100%)}
.motto{left:0;top:88px;width:282px;height:30px;background:var(--slate);color:#fff;font-weight:700;font-size:12.5px;padding:8px 0 0 38px;letter-spacing:.2px}
.intro-band{left:32px;top:269px;width:493px;height:56px;background:var(--navy);color:#fff;font-size:9.8px;line-height:11.6px;padding:10px 20px 0 32px}
.section-title{font-size:16.5px;font-weight:700;color:var(--green)}
.body-copy{font-size:9.6px;line-height:11.8px;color:var(--ink)}
.body-copy p+p{margin-top:4px}
.facts{left:34px;top:439px;width:460px;border-collapse:collapse;font-size:8px;line-height:9.6px}
.facts th{background:var(--green);color:#fff;font-size:12px;text-align:left;padding:3px 6px;height:21px;border-right:2px solid #fff}
.facts td{vertical-align:top;padding:5px 8px 5px 10px;border-right:2px solid #fff}
.facts tr:nth-child(odd) td{background:var(--row-a)}
.facts tr:nth-child(even) td{background:var(--row-b)}
.facts td:first-child{width:150px;font-weight:700}
.facts ul{margin:4px 0 0 20px}
.foot{left:0;bottom:0;width:525px;height:23px;background:var(--sky);color:var(--slate);font-size:8.5px;letter-spacing:2.6px;text-align:center;line-height:23px}
.tips-panel{left:0;top:0;width:525px;height:222px;background:var(--sky)}
.tips-tab{left:0;top:26px;width:333px;height:35px;background:var(--green);color:#fff;font-weight:700;font-size:12px;padding:11px 0 0 29px}
.tips{left:58px;top:76px;width:440px;list-style:none;color:#fff;font-size:9.6px;line-height:11.4px}
.tips li{display:flex;gap:12px;margin-bottom:7px}
.tips .num{flex:0 0 13px;height:13px;border:1px solid #fff;border-radius:50%;font-size:8px;text-align:center;line-height:11px}
.summary-tab{left:257px;top:206px;width:268px;height:29px;background:#858688;color:#fff;font-weight:700;font-size:16.5px;padding:5px 0 0 36px}
.flow{left:0;top:0;width:525px;height:679px}
.node{position:absolute;color:#fff;font-size:7.3px;line-height:8.6px;padding:10px 8px;border-radius:3px}
.node--green{background:var(--green)}
.node--blue{background:var(--sky-deep)}
.node--dark{background:var(--box-dark)}
.flow-label{position:absolute;font-size:8px;font-weight:700;color:var(--ink)}
.help{left:29px;top:481px;width:460px;border-left:3px solid var(--slate);padding-left:9px}
.help h2{font-size:16.5px;font-weight:700;color:var(--sky-deep);margin-bottom:6px}
.call{left:0;top:553px;width:525px;text-align:center;font-size:9.8px;line-height:12px}
</style>
</head>
<body>

<section class="page page--front">
  <div class="abs brand" style="left:34px;top:22px">
    <span class="brand__dot"></span>
    <div><div class="brand__name">NORTHBAY ADVISORY</div><div class="brand__tag">Restructuring &amp; Solvency Accountants</div></div>
  </div>
  <ul class="abs contact" style="left:377px;top:26px">
    <li><svg viewBox="0 0 10 10"><circle cx="5" cy="5" r="4.5" fill="none" stroke="#5d5e60"/></svg>www.northbayadvisory.example</li>
    <li><svg viewBox="0 0 10 10"><rect x="0" y="2" width="10" height="6"/></svg>info@northbayadvisory.example</li>
    <li><svg viewBox="0 0 10 10"><path d="M2 0h2l1 3-1.5 1a6 6 0 0 0 2.5 2.5L7 5l3 1v2a2 2 0 0 1-2 2A8 8 0 0 1 0 2a2 2 0 0 1 2-2z"/></svg><strong>(02) 5550 1234</strong></li>
  </ul>
  <div class="abs hero" role="img" aria-label="Photograph of a harbour city skyline with an arch bridge at sunset"></div>
  <div class="abs motto">INDEPENDENT. CONCISE. EFFICIENT.</div>
  <div class="abs intro-band">Company directors and their advisors need to be aware that non-lodgement of Business Activities Statements (“BAS”) and Superannuation Guarantee Charge (“SCG”) Statements with the ATO may be personally liability for these debts.</div>
  <h1 class="abs section-title" style="left:35px;top:337px">Director Penalty Notices (“DPN”)</h1>
  <div class="abs body-copy" style="left:36px;top:362px;width:460px">
    <p>The ATO uses DPNs and Garnishee Notices to recovery tax debts and to impose positive obligations on Directors to deal with outstanding PAYG Withholding and the Superannuation Guarantee Charge debts (“Tax Debts”).</p>
    <p>The DPN regime makes directors of companies who fail to pay Tax Debts personally liable. The key facts of DPN regime are outlined below:</p>
  </div>
  <table class="abs facts">
    <thead><tr><th>Facts</th><th>Key facts of a Directors Penalty Notice</th></tr></thead>
    <tbody>
      <tr><td>1. Director personal liabilities</td><td>Directors become personally liable for Tax Debts 21 days are the DPN Notice is issued</td></tr>
      <tr><td>2. Automatic liability for unreported and unpaid Tax Debts</td><td>Where a company’s Tax Debts were both unreported and unpaid 3 months after the due date, the directors are automatically personally liable for the Tax Debts.</td></tr>
      <tr><td>3. Avoiding personal liability for directors once they receive a DPN</td><td>Within 21 days of issuing the DPN (which may be received a week or more after issue), a director can avoid personal liability by either:
        <ul><li>Paying the Tax Debt</li><li>Appointing an Administrator to the company</li><li>Appointing a Liquidator to the company.</li></ul></td></tr>
      <tr><td>4. Effect on new directors</td><td>New directors are liable if outstanding Tax Debts are unpaid 30 days after their appointment as director</td></tr>
      <tr><td>5. Time frames</td><td>ATO can only enforce a DPN after 21 days of giving notice to the director and notice can be given to the company tax agent</td></tr>
    </tbody>
  </table>
  <div class="abs foot">www.northbayadvisory.example</div>
</section>

<section class="page page--back">
  <div class="abs tips-panel"></div>
  <div class="abs tips-tab">Tips for directors to limit or avoid personal liability:</div>
  <ol class="abs tips">
    <li><span class="num">1</span><span>Always lodge BAS and SGC Statements within 3 months of the due date, even if the liability cannot be paid!</span></li>
    <li><span class="num">2</span><span>Act immediately upon receipt of a DPN and consider a payment arrangement with the ATO. This should be considered with care as payments made can be considered as preference payments to the ATO, if a liquidator is appointed. The ATO can make the directors personally liable for the ATO preference claim</span></li>
    <li><span class="num">3</span><span>Seek professional advice from an insolvency practitioner about the options available and possibly save the company through a financial restructure.</span></li>
  </ol>
  <div class="abs summary-tab">Summary of the DPN</div>

  <svg class="abs flow" viewBox="0 0 525 679" aria-hidden="true">
    <defs><marker id="head" markerWidth="6" markerHeight="6" refX="5" refY="3" orient="auto"><path d="M0 0L6 3L0 6z" fill="#3a3a3c"/></marker></defs>
    <g fill="none" stroke="#3a3a3c" stroke-width="1">
      <path d="M124 364H148" marker-end="url(#head)"/>
      <path d="M192 310V268H305V283" marker-end="url(#head)"/>
      <path d="M192 422V467H305V447" marker-end="url(#head)"/>
      <path d="M347 315H368" marker-end="url(#head)"/>
      <path d="M391 357V416H349" marker-end="url(#head)"/>
      <path d="M441 357V375" marker-end="url(#head)"/>
    </g>
  </svg>
  <div class="node node--green" style="left:38px;top:329px;width:85px;height:68px;padding-top:22px">Issued Director’s Penalty Notice By ATO</div>
  <div class="node node--blue" style="left:151px;top:310px;width:85px;height:112px;padding-top:20px">Business Activity Statement and Superannuation Guarantee Charge lodged within 3 months from due date</div>
  <div class="node node--dark" style="left:261px;top:286px;width:85px;height:69px;padding-top:14px">Director not personally liable yet. (Have options) [RIGHTS</div>
  <div class="node node--dark" style="left:261px;top:375px;width:85px;height:69px;padding-top:22px">Director Automatically personally liable</div>
  <div class="node node--green" style="left:371px;top:265px;width:115px;height:92px;padding-top:15px">If Directors act within 21 days and:<br>1. Wind up Company voluntarily; or<br>2. Appoint Voluntary Administrator; or<br>3. Pay debt in full</div>
  <div class="node node--green" style="left:401px;top:378px;width:85px;height:69px;padding-top:16px">Director not personally liable but the company is still insolvent.</div>
  <span class="flow-label" style="left:291px;top:274px">NO</span>
  <span class="flow-label" style="left:293px;top:447px">YES</span>
  <span class="flow-label" style="left:452px;top:363px">YES</span>
  <span class="flow-label" style="left:372px;top:401px">NO</span>

  <div class="abs help">
    <h2>How Northbay Advisory can help?</h2>
    <p class="body-copy">Northbay Advisory is a firm that specialises in insolvency and restructuring, we are here to assist your clients who experiencing financial difficulties with straight forward solutions in simple to understand terms. The initial consultation is free, strictly confidential and without obligation.</p>
  </div>
  <p class="abs call">Please call <strong>(02) 5550 1234</strong> to speak to one of our solvency specialistor<br>email <strong>info@northbayadvisory.example</strong></p>
  <div class="abs brand" style="left:180px;top:593px">
    <span class="brand__dot"></span>
    <div><div class="brand__name">NORTHBAY ADVISORY</div><div class="brand__tag">Restructuring &amp; Solvency Accountants</div></div>
  </div>
  <div class="abs foot">www.northbayadvisory.example</div>
</section>

</body>
</html>
```